Business Card Design

I need a business card design. I am a sole practitioner.I am a psychotherapist and I need a professional card. I am also an art therapist (a form of psychotherapy using art) so I want the image to be professional/creative/maybe ethnic. I do not want a boring minimalist "medical" image, nor do I want it too hippy/tree hugging.
Colours like reds/ochres/yellows would be good.
Industry/Entity Type
Business
Contact Information for Business Card
Mira Tanvel
Psychotherapy, Counselling and Art Therapy
Korrabel Lodge Counselling and Wellbeing services
17 Farrow Lane, Pelbury 4091
0419362750 www.MiraTanvel.com.au
on rear of card I need the option to have at least 4 or 5 appointment times /dates
Look and feel
Each slider illustrates characteristics of the customer's brand and the style your logo design should communicate.

```html
<!DOCTYPE html>
<html lang="en">
<head>
<meta charset="utf-8">
<title>Mira Tanvel – Business Card</title>
<link href="https://fonts.googleapis.com/css2?family=Andika:wght@400;700&family=Courgette&display=swap" rel="stylesheet">
<style>
  :root {
    --backdrop: #e6e6e8;
    --ochre: #b8955a;
    --ochre-light: #c9a66b;
    --gold-text: #c99a45;
    --charcoal: #2f2b30;
    --brown-ink: #4a3216;
    --paper: #ffffff;
  }
  * { margin: 0; padding: 0; box-sizing: border-box; }
  html, body { width: 1200px; height: 800px; overflow: hidden; }
  body {
    background: var(--backdrop);
    font-family: "Andika", "Trebuchet MS", sans-serif;
    position: relative;
  }
  .card {
    position: absolute;
    top: 250px;
    width: 520px;
    height: 297px;
    overflow: hidden;
    box-shadow: 0 6px 18px rgba(0,0,0,0.18);
  }

  /* Back side: appointment card */
  .card--back { left: 50px; background: var(--paper); color: var(--brown-ink); }
  .appointment__title {
    position: absolute; top: 26px; width: 100%;
    text-align: center; font-size: 19px; font-weight: 700;
  }
  .appointment__rows { position: absolute; top: 62px; left: 56px; list-style: none; }
  .appointment__row { font-size: 15px; font-weight: 700; height: 27px; line-height: 27px; letter-spacing: 0.3px; }
  .back__stripe { position: absolute; left: 0; width: 100%; background: var(--ochre); }
  .back__stripe--upper { top: 114px; height: 10px; }
  .back__stripe--lower { top: 212px; height: 26px; }
  .back__web { position: absolute; top: 186px; right: 28px; font-size: 14px; }
  .back__email { position: absolute; top: 216px; left: 28px; font-size: 14px; color: var(--brown-ink); }
  .back__address {
    position: absolute; top: 246px; width: 100%;
    text-align: center; font-size: 14.5px; font-weight: 700; line-height: 19px;
  }

  /* Front side */
  .card--front { left: 630px; background: var(--charcoal); }
  .front__shapes { position: absolute; inset: 0; }
  .front__pattern {
    position: absolute; left: 36px; top: 34px; width: 118px; height: 118px;
    border: 3px solid var(--ochre-light);
    background: linear-gradient(135deg, #3a3236, #8a6d3e 55%, #2f2b30);
  }
  .front__name {
    position: absolute; top: 30px; left: 262px;
    font-family: "Courgette", cursive; font-size: 40px; color: var(--charcoal);
  }
  .front__discipline {
    position: absolute; top: 84px; left: 262px;
    font-family: "Courgette", cursive; font-size: 14px; color: var(--charcoal);
  }
  .front__phone {
    position: absolute; top: 150px; right: 36px;
    font-size: 26px; font-weight: 700; color: var(--gold-text); letter-spacing: 0.5px;
  }
  .front__contact {
    position: absolute; top: 190px; left: 36px;
    font-size: 14px; line-height: 19px; color: var(--gold-text);
  }
  .front__address {
    position: absolute; top: 238px; width: 100%;
    text-align: center; font-size: 14px; line-height: 18px; color: var(--gold-text);
  }
</style>
</head>
<body>

  <section class="card card--back" aria-label="Appointment side">
    <h2 class="appointment__title">Appointment</h2>
    <div class="back__stripe back__stripe--upper"></div>
    <ul class="appointment__rows">
      <li class="appointment__row">Date ..../..../........&nbsp; Time ..........a.m/p.m</li>
      <li class="appointment__row">Date ..../..../........&nbsp; Time ..........a.m/p.m</li>
      <li class="appointment__row">Date ..../..../........&nbsp; Time ..........a.m/p.m</li>
      <li class="appointment__row">Date ..../..../........&nbsp; Time ..........a.m/p.m</li>
    </ul>
    <p class="back__web">www.miratanvel.com.au</p>
    <div class="back__stripe back__stripe--lower"></div>
    <p class="back__email">miratanvel@korrmail.com</p>
    <p class="back__address">Korrabel Lodge Counselling &amp; Wellbeing Services<br>17 Farrow Lane, Pelbury, 4091</p>
  </section>

  <section class="card card--front" aria-label="Front side">
    <svg class="front__shapes" viewBox="0 0 520 297" width="520" height="297" aria-hidden="true">
      <path d="M0 0 H520 V112 C440 116 380 120 330 122 C300 124 280 150 240 152 H0 Z" fill="var(--ochre)"/>
      <path d="M0 152 H240 C280 150 300 124 330 122 C380 120 440 116 520 112" fill="none" stroke="var(--ochre-light)" stroke-width="2"/>
      <line x1="0" y1="284" x2="520" y2="284" stroke="var(--ochre-light)" stroke-width="2"/>
    </svg>
    <div class="front__pattern" role="img" aria-label="Square panel of flowing bands and spiral motifs in gold on charcoal"></div>
    <h1 class="front__name">Mira Tanvel</h1>
    <p class="front__discipline">Psychotherapy and Counselling</p>
    <p class="front__phone">0419 362750</p>
    <p class="front__contact">miratanvel@korrmail.com<br>www.miratanvel.com.au</p>
    <p class="front__address">Korrabel Lodge Counselling &amp; Wellbeing Services<br>17 Farrow Lane, Pelbury, 4091</p>
  </section>

</body>
</html>
```